Business Card for Medical Laboratory Data Processor
logo design just finished
Use same font as used in my logo
Marcel Ondrak, MBA, CNE, MCSE
Chief Technology Officer
47 Fenwick Ave
Ann Arbor, MI 48103
marcel.ondrak@threlgo.com
www.threlgo.com
we would like business card to use same look/logo as the attached new logo. Using the same font is good, but optional.
We are interested in including a QR code on either front or back of the card.
AI Files for new logo. (from just finished contest)

```html
<!DOCTYPE html>
<html lang="en">
<head>
<meta charset="utf-8">
<title>Threlgo Business Card</title>
<link href="https://fonts.googleapis.com/css2?family=Exo+2:wght@400;600&display=swap" rel="stylesheet">
<style>
  :root {
    --stage: #e6e7e9;
    --card-black: #050607;
    --card-charcoal: #1a1c1f;
    --brand-blue: #1f7fd1;
    --deep-blue: #0d4f93;
    --brand-green: #6cc12c;
    --text-light: #f2f4f6;
    --text-muted: #9aa3ad;
  }
  * { margin: 0; padding: 0; box-sizing: border-box; }
  html, body {
    width: 1200px;
    height: 1009px;
    overflow: hidden;
    background: var(--stage);
    font-family: "Exo 2", sans-serif;
  }
  .sheet {
    width: 1200px;
    height: 1009px;
    display: flex;
    flex-direction: column;
    align-items: center;
    justify-content: center;
    gap: 26px;
  }
  .card {
    position: relative;
    width: 820px;
    height: 469px;
    border-radius: 22px;
    overflow: hidden;
    background: radial-gradient(ellipse at 50% 40%, var(--card-charcoal) 0%, var(--card-black) 70%);
    box-shadow: 0 6px 18px rgba(0,0,0,0.22);
  }
  .brand {
    display: flex;
    align-items: center;
    gap: 14px;
    color: var(--brand-blue);
    font-weight: 600;
    letter-spacing: 6px;
  }
  .brand-dot {
    width: 18px;
    height: 18px;
    border-radius: 50%;
    background: var(--brand-green);
  }
  /* back side */
  .card-back .brand {
    position: absolute;
    left: 50%;
    top: 170px;
    transform: translateX(-50%);
    font-size: 58px;
  }
  .card-back .web {
    position: absolute;
    left: 0;
    right: 0;
    top: 290px;
    text-align: center;
    color: var(--text-muted);
    font-size: 17px;
    letter-spacing: 7px;
  }
  /* front side */
  .swoosh {
    position: absolute;
    inset: 0;
    width: 100%;
    height: 100%;
  }
  .card-front .brand {
    position: absolute;
    left: 380px;
    top: 95px;
    font-size: 56px;
  }
  .contact {
    position: absolute;
    left: 38px;
    top: 238px;
    list-style: none;
    color: var(--text-light);
    font-size: 16px;
    line-height: 29px;
    letter-spacing: 0.6px;
  }
  .contact li {
    display: flex;
    align-items: center;
    gap: 12px;
  }
  .contact svg {
    width: 16px;
    height: 16px;
    fill: var(--text-light);
    flex: none;
  }
  .holder {
    position: absolute;
    right: 34px;
    bottom: 40px;
    text-align right;
    text-align: right;
    color: var(--text-light);
  }
  .holder-name {
    font-size: 17px;
    letter-spacing: 1.2px;
  }
  .holder-title {
    margin-top: 4px;
    font-size: 13px;
    letter-spacing: 1.5px;
    color: var(--text-muted);
  }
</style>
</head>
<body>
<main class="sheet">

  <section class="card card-back">
    <div class="brand"><span class="brand-dot"></span><span class="brand-name">THRELGO</span></div>
    <p class="web">WWW.THRELGO.COM</p>
  </section>

  <section class="card card-front">
    <svg class="swoosh" viewBox="0 0 820 469" preserveAspectRatio="none" aria-hidden="true">
      <defs>
        <linearGradient id="blueFill" x1="0" y1="0" x2="1" y2="1">
          <stop offset="0" stop-color="#2a8fe0"/>
          <stop offset="1" stop-color="#0d4f93"/>
        </linearGradient>
        <linearGradient id="greenBand" x1="0" y1="0" x2="1" y2="0">
          <stop offset="0" stop-color="#4fa51e"/>
          <stop offset="0.6" stop-color="#7fd236"/>
          <stop offset="1" stop-color="#4fa51e"/>
        </linearGradient>
      </defs>
      <path d="M0,112 C268,112 414,244 452,469 L0,469 Z" fill="url(#blueFill)"/>
      <path d="M0,98 C280,98 430,230 470,469" fill="none" stroke="url(#greenBand)" stroke-width="16"/>
      <path d="M0,124 C256,126 398,256 436,469" fill="none" stroke="#0a3f78" stroke-width="3" opacity="0.6"/>
    </svg>

    <div class="brand"><span class="brand-dot"></span><span class="brand-name">THRELGO</span></div>

    <ul class="contact">
      <li><svg viewBox="0 0 16 16"><path d="M8 1a5 5 0 0 0-5 5c0 4 5 9 5 9s5-5 5-9a5 5 0 0 0-5-5zm0 7a2 2 0 1 1 0-4 2 2 0 0 1 0 4z"/></svg>47 Fenwick Ave</li>
      <li><svg viewBox="0 0 16 16"><path d="M8 1a5 5 0 0 0-5 5c0 4 5 9 5 9s5-5 5-9a5 5 0 0 0-5-5zm0 7a2 2 0 1 1 0-4 2 2 0 0 1 0 4z"/></svg>Ann Arbor, MI 48103</li>
      <li><svg viewBox="0 0 16 16"><path d="M4 1h3l1 4-2 1c1 2 2 3 4 4l1-2 4 1v3c0 1-1 2-2 2C7 14 2 9 2 3c0-1 1-2 2-2z"/></svg>800-555-0187</li>
      <li><svg viewBox="0 0 16 16"><path d="M4 1h3l1 4-2 1c1 2 2 3 4 4l1-2 4 1v3c0 1-1 2-2 2C7 14 2 9 2 3c0-1 1-2 2-2z"/></svg>734-555-0142</li>
      <li><svg viewBox="0 0 16 16"><path d="M1 3h14v10H1zm1 1v.5l6 4 6-4V4z"/></svg>marcel.ondrak@threlgo.com</li>
      <li><svg viewBox="0 0 16 16"><path d="M8 1a7 7 0 1 0 0 14A7 7 0 0 0 8 1zm0 1.5c.8 0 1.8 1.6 2 4.5H6c.2-2.9 1.2-4.5 2-4.5zM6 8.5h4c-.2 2.9-1.2 4.5-2 4.5s-1.8-1.6-2-4.5z"/></svg>www.threlgo.com</li>
    </ul>

    <div class="holder">
      <p class="holder-name">Marcel Ondrak, MBA, CNE, MCSE</p>
      <p class="holder-title">Chief Technology Officer</p>
    </div>
  </section>

</main>
</body>
</html>
```